Contact card for an aggressive entrepreneur

I am looking for a business/contact card as an individual. I operate under the company name The Varden Collective, LLC (but don't generally use that other than for billing). I have explored a few ideas and am now turning to artplaza to connect with people more creative than me. I am trying to capture a diverse set of passions, which I will summarize with the following keywords (which may or may not be ON the card and are in no particular order):

entrepreneur
shark diver
MBA
visionary
defenseman
marketing guru
hockey coach
teacher
reader
writer
cook
captain
scuba diver
beach bum
Type A
Brightwater
Vermont
New York
Montauk
founder
leader
focused
driven
teammate father

hope that makes some sense!
Updates

Please note the photo is for reference - unless there is a really creative way to use it I do not need a card with a head shot (I am not a model or an actor!)

Project Deadline Extended
Reason: There have been several requests to submit designs so we will close this project this Wednesday and select a design by this Friday. Thank you to all for your great ideas and submissions!

I am reviewing the designs and will select one by end of day tomorrow, Tuesday, EST
Thank you to all who participated!

Target Market(s)

everyone from business contacts to personal acquaintances

Industry/Entity Type

Business

Requirements
Must have
• Must be utterly original, extraordinary and memorable.
How it achieves that is up to you!
Essential contact information that needs to be included:

phone: (555) 374-1926
email: tomas@vardencollective.example
skype: tomas.varden
Nice to have
• A striking visual whether that is a photo or illustration
Some way of conveying the diversity of what I am and what I do
Feel free to use the printing or physical material of the card to make it stand out.
Should not have
• I am not into "logos" but that being said I do not want to limit creativity in any way so feel free to ignore any part of this brief if you disagree with me. No need to use the attached photo of me, but that's what I look like.

```html
<!DOCTYPE html>
<html lang="en">
<head>
<meta charset="utf-8">
<title>Tomas Varden – Contact Card</title>
<link rel="stylesheet" href="https://fonts.googleapis.com/css2?family=PT+Sans:wght@400;700&display=swap">
<style>
  :root {
    --stage: #bcbdbf;
    --card-back: #ffffff;
    --texture-light: #f4f4f4;
    --texture-mid: #e9e9e9;
    --ink: #111111;
    --label: #ffffff;
    --photo-light: #6a5a48;
    --photo-mid: #2e2a26;
    --photo-dark: #0d0c0b;
    --shadow: rgba(0,0,0,0.45);
  }
  * { margin: 0; padding: 0; box-sizing: border-box; }
  html, body {
    width: 934px; height: 1200px; overflow: hidden;
    background: var(--stage);
    font-family: "PT Sans", "Myriad Pro", Arial, sans-serif;
  }
  .stage { position: relative; width: 934px; height: 1200px; }

  .card {
    position: absolute;
    top: 324px;
    overflow: hidden;
    box-shadow: 8px 8px 9px var(--shadow);
  }

  /* Front: portrait with keyword column */
  .card--front {
    left: 135px; width: 285px; height: 512px;
  }
  .card__portrait {
    position: absolute; inset: 0;
    background:
      radial-gradient(ellipse 60% 40% at 20% 8%, #c9a46a 0%, rgba(201,164,106,0) 70%),
      radial-gradient(ellipse 35% 22% at 42% 22%, #b98a6e 0%, rgba(185,138,110,0) 75%),
      linear-gradient(180deg, var(--photo-light) 0%, var(--photo-mid) 45%, var(--photo-dark) 100%);
  }
  .keyword-list {
    position: absolute;
    right: 17px; top: 28px;
    list-style: none;
    text-align: right;
    color: var(--label);
    font-size: 10px;
    line-height: 19.5px;
  }

  /* Back: soft texture field with contact details */
  .card--back {
    left: 512px; width: 287px; height: 515px;
    background: var(--card-back);
  }
  .card__texture {
    position: absolute; inset: 0;
    background: linear-gradient(180deg, var(--texture-light) 0%, var(--texture-mid) 50%, var(--texture-light) 100%);
  }
  .contact {
    position: absolute;
    left: 0; right: 0; top: 222px;
    text-align: center;
    color: var(--ink);
    font-size: 17px;
    font-weight: 700;
    line-height: 22.5px;
  }
</style>
</head>
<body>
<div class="stage">

  <section class="card card--front">
    <div class="card__portrait" role="img" aria-label="Portrait photograph of the card owner in a dark suit and tie, leaning on one arm in a softly lit office"></div>
    <ul class="keyword-list">
      <li>entrepreneur</li>
      <li>shark diver</li>
      <li>MBA</li>
      <li>visionary</li>
      <li>defenseman</li>
      <li>marketing guru</li>
      <li>hockey coach</li>
      <li>teacher</li>
      <li>reader</li>
      <li>writer</li>
      <li>cook</li>
      <li>captain</li>
      <li>scuba diver</li>
      <li>beach bum</li>
      <li>Type A</li>
      <li>Brightwater</li>
      <li>Vermont</li>
      <li>New York</li>
      <li>Montauk</li>
      <li>founder</li>
      <li>leader</li>
      <li>focused</li>
      <li>driven</li>
      <li>teammate father</li>
    </ul>
  </section>

  <section class="card card--back">
    <div class="card__texture" role="img" aria-label="Faint light-grey typographic texture filling the whole card back"></div>
    <div class="contact">
      <p class="contact__phone">(555) 374-1926</p>
      <p class="contact__email">tomas@vardencollective.example</p>
      <p class="contact__skype">tomas.varden</p>
    </div>
  </section>

</div>
</body>
</html>
```